TalkWell needs a Letterhead

We need a letterhead for our company "TalkWell Consultants". Logo is attached. The company color is Turquoise. Icons for website, scan logo for website, icons for address, e-mail and phone appreciated rather than just words.

```html
<!DOCTYPE html>
<html lang="en">
<head>
<meta charset="utf-8">
<title>TalkWell Consultants Letterhead</title>
<link rel="stylesheet" href="https://fonts.googleapis.com/css2?family=Open+Sans:wght@400;600&display=swap">
<style>
  :root {
    --backdrop: #555555;
    --paper: #ffffff;
    --brand-blue: #2e95d0;
    --brand-green: #5bb847;
    --brand-orange: #d2642c;
    --ink: #222222;
    --rule: #9a9a9a;
  }
  * { margin: 0; padding: 0; box-sizing: border-box; }
  html, body {
    width: 1200px;
    height: 1000px;
    overflow: hidden;
    background: var(--backdrop);
    font-family: "Open Sans", Arial, sans-serif;
  }
  .letterhead {
    position: absolute;
    left: 293px;
    top: 105px;
    width: 614px;
    height: 790px;
    background: var(--paper);
    box-shadow: 0 2px 6px rgba(0,0,0,0.35);
  }
  .top-bar {
    position: absolute;
    left: 0; top: 0;
    width: 100%;
    height: 6px;
    background: var(--brand-blue);
  }
  .brand {
    position: absolute;
    left: 36px;
    top: 40px;
    display: flex;
    align-items: center;
    gap: 10px;
    color: var(--brand-orange);
    font-weight: 400;
  }
  .brand-mark {
    width: 26px;
    height: 26px;
    background: var(--brand-blue);
  }
  .brand-name {
    display: flex;
    flex-direction: column;
    line-height: 1;
  }
  .brand-name .word { font-size: 24px; letter-spacing: -0.2px; }
  .brand-name .tagline { font-size: 9.5px; letter-spacing: 2.6px; margin-top: 2px; padding-left: 22px; }
  .contact {
    position: absolute;
    left: 473px;
    top: 30px;
    padding-left: 8px;
    border-left: 1px solid var(--rule);
    list-style: none;
    font-size: 7px;
    color: var(--ink);
    line-height: 1;
  }
  .contact li {
    display: flex;
    align-items: flex-start;
    gap: 4px;
    margin: 3px 0 2px;
  }
  .contact svg { width: 9px; height: 9px; flex: none; }
  .contact .address { line-height: 1.2; }
  .footer-band {
    position: absolute;
    left: 0;
    bottom: 0;
    width: 614px;
    height: 13px;
  }
</style>
</head>
<body>
  <main class="letterhead">
    <div class="top-bar"></div>

    <header class="brand">
      <span class="brand-mark"></span>
      <span class="brand-name">
        <span class="word">TalkWell</span>
        <span class="tagline">CONSULTANTS</span>
      </span>
    </header>

    <ul class="contact">
      <li>
        <svg viewBox="0 0 9 9"><rect width="9" height="9" rx="1.5" fill="var(--brand-blue)"/><circle cx="4.5" cy="4.5" r="2.8" fill="none" stroke="#fff" stroke-width="0.8"/><line x1="1.7" y1="4.5" x2="7.3" y2="4.5" stroke="#fff" stroke-width="0.6"/><ellipse cx="4.5" cy="4.5" rx="1.2" ry="2.8" fill="none" stroke="#fff" stroke-width="0.6"/></svg>
        <span>www.talkwellsite.com</span>
      </li>
      <li>
        <svg viewBox="0 0 9 9"><rect width="9" height="9" rx="1.5" fill="var(--brand-blue)"/><rect x="1.8" y="2.6" width="5.4" height="3.8" fill="none" stroke="#fff" stroke-width="0.7"/><polyline points="1.8,2.6 4.5,4.8 7.2,2.6" fill="none" stroke="#fff" stroke-width="0.7"/></svg>
        <span>hello@talkwellsite.com</span>
      </li>
      <li>
        <svg viewBox="0 0 9 9"><rect width="9" height="9" rx="1.5" fill="var(--brand-blue)"/><path d="M3 1.8 L4 3.6 L3.3 4.3 Q4 5.6 5 6 L5.6 5.3 L7.2 6.2 L6.6 7.3 Q3.5 7 2 3 Z" fill="#fff"/></svg>
        <span>00 5519 0374</span>
      </li>
      <li>
        <svg viewBox="0 0 9 9"><rect width="9" height="9" rx="1.5" fill="var(--brand-blue)"/><path d="M4.5 1.5 A2.2 2.2 0 0 1 6.7 3.7 Q6.7 5 4.5 7.6 Q2.3 5 2.3 3.7 A2.2 2.2 0 0 1 4.5 1.5 Z" fill="#fff"/><circle cx="4.5" cy="3.7" r="0.8" fill="var(--brand-blue)"/></svg>
        <span class="address">48 Harbor Lane - Eastfield<br>PO Box 5678, Town Name</span>
      </li>
    </ul>

    <svg class="footer-band" viewBox="0 0 614 13" preserveAspectRatio="none" aria-hidden="true">
      <path d="M0 0 H370 C398 0 414 5 426 13 H0 Z" fill="var(--brand-blue)"/>
      <path d="M404 0 H614 V13 H446 C436 6 424 1 404 0 Z" fill="var(--brand-green)"/>
    </svg>
  </main>
</body>
</html>
```